【サイトマップ】
1 TOP
2 Rulavekとは
3 お客様の声(一覧)
4 お客様の声(詳細)
5 ブログ(一覧)
6 ブログ(詳細)
7 お知らせ(一覧)
8 お知らせ(詳細)
9 イベント情報(一覧)
10 イベント情報(詳細)
11 お問い合わせ
12 Q&A
13 商品ページ(一覧)
14 商品ページ(詳細)
15 ライター紹介ページ

【要望】
情報発信サイトのため静的なページは最低限押さえ動的なコンテンツを盛り込んでおります。
各ページの意図を説明しておきます。

<ブログ>
いわゆるコラムページです。季節に合わせた着こなしやおすすめのコーディネートなどを紹介していきます。

<お客様の声>
商品レビュー。ECで購入した商品についてお客様の感想を掲載します。

<イベント情報>
着こなし講座。お食事会などイベントについて掲載していきます。

<商品ページ>
ライターが連動しているECサイトから商品をピックアップし記事として取り上げます。

<ライター紹介ページ>
まずはライターは2名体勢で指導しますが今後増やしていく予定です。
TOPに2名分の枠を用意頂ければと思います。
参考:https://brevhaus.co.jp/member

■HPのメインターゲット
30、40代の方(女性のみ)

■サイトのデザインにおける優先事項
見やすさ > デザイン性(写真・画像量)

■HPに望む効果
・新規顧客獲得
ECサイトも立ち上げ前なので、とにかくサイトのファンを付けたいと考えております。
そのため「人目につくサイト」「定期的にチェックしてみたいと思ってもらえるサイト」を目指しております。
希望イメージ
シンプル 複雑
単色 カラフル
暗い 明るい
日常 高級
遊び心 厳粛
未来的 伝統的
女性的 男性的
希望する色
特にございません。いろんな提案を見てみたいのが正直なところです。
納品ファイル
• イラストレーター形式 (.ai)
• フォトショップ形式 (.psd)
• PNG形式 (.png)
補足説明
<店舗へのご連絡はおやめください>
クレフォスの規約にもありますが、店舗様の通常業務に支障が出るため・素材について直接電話等のお問い合わせをお控えいただきますよう、ご協力の程お願いいたします。

-----------------------------------------------------------------------

<素材はPixoranかその他無償の素材をご使用ください>
素材として必要なものがある場合にはピクソラン画像をご使用ください。
疑問や不明点などがありましたら、クレフォス内メッセージにて頂戴できますと幸いです。

その際、定期契約でダウンロード出来る画像のみを使用してください。
(画像検索した際に出てくるサムネール下の画像番号の横に
ピクソランのマークがあるものは使用しないようお願いいたします。)

ピクソラン以外の素材を使用する際には、
必ず無料で提供いただける物のみご使用ください。
もう少し提案を見たいため延長させて頂きます。
もう少し提案が見たいため、延長させて頂きます。
本日より1週間募集期間を延長致します。
引き続き宜しくお願い致します。
沢山のご提案をありがとうございます。
最後にあと一週間だけ期間を延長させていただきます。
引き続き、何卒宜しくお願い致します。

ひと目見て気に入りました。

みなさまご提案ありがとうございました。

```html
<!DOCTYPE html>
<html lang="ja">
<head>
<meta charset="utf-8">
<title>Rulavek</title>
<link href="https://fonts.googleapis.com/css2?family=Josefin+Sans:wght@300;400;600&family=Noto+Sans+JP:wght@400;500&display=swap" rel="stylesheet">
<style>
:root{
  --olive:#b0982c;
  --olive-dark:#8f7b1f;
  --beige:#f1ece1;
  --text:#333;
  --muted:#888;
  --line:#ddd6c6;
  --red:#c0392b;
  --white:#fff;
}
*{box-sizing:border-box;margin:0;padding:0}
html,body{width:1200px;height:2384px;overflow:hidden;background:var(--white)}
body{position:relative;font-family:"Noto Sans JP",sans-serif;color:var(--text);font-size:11px;line-height:1.6}

/* header */
.site-header{position:absolute;left:0;top:0;width:784px;height:80px}
.wordmark{position:absolute;left:228px;top:20px;display:flex;align-items:center;gap:7px;font-family:"Noto Sans JP",sans-serif;font-weight:500;font-size:15px;letter-spacing:2px;color:var(--text)}
.wordmark::before{content:"";width:9px;height:9px;background:var(--olive);display:block}
.social{position:absolute;left:690px;top:26px;display:flex;gap:10px}
.social span{width:12px;height:12px;background:var(--olive);display:block}

/* hero */
.hero{position:absolute;left:0;top:80px;width:1200px;height:380px}
.hero .slide{position:absolute;top:0;height:380px}
.slide-left{left:0;width:220px;background:linear-gradient(135deg,#d9d6d2,#8e8a86)}
.slide-main{left:228px;width:532px;background:linear-gradient(120deg,#c9c2b6,#6f6a62 60%,#3e3a36)}
.slide-right{left:976px;width:224px;background:linear-gradient(180deg,#b84a3a,#3f6e4c 55%,#d7c8a8)}
.slide-main .caption{position:absolute;left:0;right:0;bottom:0;padding:16px 24px 20px;background:rgba(0,0,0,.35);color:var(--white);font-size:12px}
.slide-main .caption .tag{position:absolute;left:24px;top:-10px;background:var(--olive);color:#fff;font-size:9px;padding:2px 8px}
.dots{position:absolute;left:480px;top:470px;display:flex;gap:6px}
.dots i{width:6px;height:6px;border-radius:50%;background:#ccc;display:block}
.dots i.on{background:var(--olive)}

/* sections */
.section{position:absolute;left:228px;width:532px}
.sec-title{text-align:center}
.sec-title h2{font-family:"Josefin Sans",sans-serif;font-weight:400;font-size:26px;letter-spacing:3px;color:var(--olive)}
.sec-title p{font-size:9px;color:var(--olive)}
.grid{display:grid;grid-template-columns:repeat(3,164px);gap:20px;margin-top:22px}
.card{position:relative}
.thumb{width:164px;height:118px;display:block}
.ribbon{position:absolute;left:0;top:0;width:0;height:0;border-top:30px solid var(--red);border-right:30px solid transparent}
.meta{display:flex;justify-content:space-between;align-items:center;margin-top:8px}
.cat{background:var(--olive);color:#fff;font-size:8px;padding:1px 10px}
.date{font-family:"Josefin Sans",sans-serif;font-size:9px;color:var(--muted)}
.card h3{font-weight:400;font-size:11px;margin-top:6px;line-height:1.6}
.more{display:block;margin:28px auto 0;width:110px;height:26px;border:1px solid var(--olive);color:var(--olive);font-family:"Josefin Sans",sans-serif;font-size:9px;letter-spacing:1px;text-align:center;line-height:26px}

.event-list{margin-top:22px}
.event{display:flex;gap:22px;height:118px;margin-bottom:20px}
.event .thumb{flex:none}
.event .body{flex:1;padding-top:4px}
.event h3{font-weight:400;font-size:13px;margin-top:8px;line-height:1.6}
.event p{font-size:10px;color:var(--muted);margin-top:8px}

/* sidebar */
.sidebar{position:absolute;left:784px;top:0;width:192px;height:2140px;background:var(--beige);padding:40px 12px 0}
.contact-btn{height:24px;background:var(--olive);color:#fff;font-family:"Josefin Sans",sans-serif;font-size:9px;letter-spacing:1px;display:flex;align-items:center;padding-left:30px;position:relative}
.contact-btn::before{content:"";position:absolute;left:10px;top:8px;width:11px;height:8px;border:1px solid #fff}
.search{margin-top:32px;height:24px;background:#fff;border:1px solid var(--line);position:relative}
.search::after{content:"";position:absolute;right:6px;top:5px;width:10px;height:12px;background:var(--olive)}
.nav{margin-top:14px;list-style:none}
.nav li{height:48px;border-bottom:1px solid var(--line);display:flex;align-items:center;justify-content:space-between;font-family:"Josefin Sans",sans-serif;font-size:10px;letter-spacing:1px;padding:0 4px}
.nav li::after{content:"";width:5px;height:5px;border-right:1px solid var(--muted);border-top:1px solid var(--muted);transform:rotate(45deg)}
.banner{margin:30px auto 0;width:96px;height:60px;border:2px solid var(--olive);background:#fff;position:relative;display:flex;align-items:center;justify-content:center}
.banner .ph{width:40px;height:40px;border-radius:50%;background:linear-gradient(#d8cbb8,#9b8a78)}
.side-title{text-align:center;margin-top:26px}
.side-title h2{font-family:"Josefin Sans",sans-serif;font-weight:400;font-size:14px;letter-spacing:2px;color:var(--olive)}
.side-title p{font-size:8px;color:var(--olive)}
.review{margin-top:16px;position:relative}
.review .img{width:168px;height:120px;display:block}
.review h3{font-weight:400;font-size:10px;margin-top:6px}
.review p{font-size:9px;color:var(--muted)}
.writers{display:flex;justify-content:center;gap:26px;margin-top:16px;text-align:center;font-size:9px}
.writers .av{width:52px;height:52px;border-radius:50%;background:linear-gradient(#d7cec2,#8f8478);margin-bottom:4px}
.keywords{display:flex;flex-wrap:wrap;gap:5px;margin-top:14px}
.keywords span{border:1px solid var(--olive);background:#fff;color:var(--olive);font-size:8px;padding:1px 6px}

/* footer */
.site-footer{position:absolute;left:0;top:2152px;width:1200px;height:232px;border-top:1px solid var(--line)}
.site-footer .wordmark{top:54px}
.site-footer .social{top:58px}
.foot-nav{position:absolute;left:228px;top:86px;display:flex;gap:150px;font-size:9px;list-style:none}
.foot-nav ul{list-style:none;line-height:1.9}
.foot-contact{position:absolute;left:796px;top:52px;width:168px}
.pagetop{position:absolute;left:1132px;top:58px;width:26px;height:26px;border:1px solid var(--line);display:flex;align-items:center;justify-content:center}
.pagetop::after{content:"";width:6px;height:6px;border-left:1px solid var(--muted);border-top:1px solid var(--muted);transform:rotate(45deg);margin-top:3px}
.copy{position:absolute;left:0;right:0;top:184px;text-align:center;font-size:8px;color:var(--muted)}

/* image tones */
.t1{background:linear-gradient(135deg,#d9d3cc,#5d5a57)}
.t2{background:linear-gradient(135deg,#e7e2d7,#a39077)}
.t3{background:linear-gradient(135deg,#c9573f,#3d6b4f 60%,#e3d5b5)}
.t4{background:linear-gradient(135deg,#e7c3c8,#b58a93)}
.t5{background:linear-gradient(135deg,#ede6df,#9a8f86)}
.t6{background:linear-gradient(135deg,#f1e6e1,#c7a39a)}
.t7{background:linear-gradient(135deg,#c7a99b,#5f4740)}
.t8{background:linear-gradient(135deg,#d98bb0,#3b3340)}
.t9{background:linear-gradient(135deg,#d9a48a,#6e5c52)}
.t10{background:linear-gradient(135deg,#e8dfd0,#b99d70)}
</style>
</head>
<body>

<header class="site-header">
  <div class="wordmark">Rulavek</div>
  <div class="social"><span></span><span></span><span></span></div>
</header>

<section class="hero">
  <div class="slide slide-left" role="img" aria-label="スライド写真:ファッション小物"></div>
  <div class="slide slide-main" role="img" aria-label="メインスライド写真:帽子をかぶった女性">
    <div class="caption"><span class="tag">BLOG</span>記事タイトル記事タイトル記事タイトル記事タイトル記事タイトル記事タイトル記事タイトル記事タイトル記事タイトル</div>
  </div>
  <div class="slide slide-right" role="img" aria-label="スライド写真:街並みの建物"></div>
</section>
<div class="dots"><i class="on"></i><i></i><i></i></div>

<section class="section" style="top:508px">
  <div class="sec-title"><h2>WHAT'S NEW</h2><p>新着情報</p></div>
  <div class="grid">
    <article class="card"><div class="thumb t1" role="img" aria-label="記事写真:コーディネート"></div><span class="ribbon"></span><div class="meta"><span class="cat">BLOG</span><span class="date">2017.00.00</span></div><h3>記事タイトル記事タイトル記事タイトル記事タイトル</h3></article>
    <article class="card"><div class="thumb t2" role="img" aria-label="記事写真:女性のファッション"></div><div class="meta"><span class="cat">EVENT</span><span class="date">2017.00.00</span></div><h3>記事タイトル記事タイトル記事タイトル記事タイトル</h3></article>
    <article class="card"><div class="thumb t3" role="img" aria-label="記事写真:街並み"></div><span class="ribbon"></span><div class="meta"><span class="cat">ITEMS</span><span class="date">2017.00.00</span></div><h3>記事タイトル記事タイトル記事タイトル記事タイトル</h3></article>
    <article class="card"><div class="thumb t1" role="img" aria-label="記事写真:コーディネート"></div><div class="meta"><span class="cat">BLOG</span><span class="date">2017.00.00</span></div><h3>記事タイトル記事タイトル記事タイトル記事タイトル</h3></article>
    <article class="card"><div class="thumb t2" role="img" aria-label="記事写真:女性のファッション"></div><div class="meta"><span class="cat">EVENT</span><span class="date">2017.00.00</span></div><h3>記事タイトル記事タイトル記事タイトル記事タイトル</h3></article>
    <article class="card"><div class="thumb t3" role="img" aria-label="記事写真:街並み"></div><div class="meta"><span class="cat">ITEMS</span><span class="date">2017.00.00</span></div><h3>記事タイトル記事タイトル記事タイトル記事タイトル</h3></article>
  </div>
</section>

<section class="section" style="top:1036px">
  <div class="sec-title"><h2>EVENT</h2><p>イベント情報</p></div>
  <div class="event-list">
    <article class="event"><div class="thumb t4" role="img" aria-label="イベント写真:花とテーブル"></div><div class="body"><div class="meta"><span class="cat">EVENT</span><span class="date">2017.00.00</span></div><h3>記事タイトル記事タイトル記事タイトル記事タイトル記事タイトル記事タイトル</h3><p>テキストテキストテキストテキストテキストテキストテキスト</p></div></article>
    <article class="event"><div class="thumb t5" role="img" aria-label="イベント写真:着こなし講座"></div><div class="body"><div class="meta"><span class="cat">EVENT</span><span class="date">2017.00.00</span></div><h3>記事タイトル記事タイトル記事タイトル記事タイトル記事タイトル記事タイトル</h3><p>テキストテキストテキストテキストテキストテキストテキスト</p></div></article>
    <article class="event"><div class="thumb t6" role="img" aria-label="イベント写真:お食事会"></div><div class="body"><div class="meta"><span class="cat">EVENT</span><span class="date">2017.00.00</span></div><h3>記事タイトル記事タイトル記事タイトル記事タイトル記事タイトル記事タイトル</h3><p>テキストテキストテキストテキストテキストテキストテキスト</p></div></article>
  </div>
  <span class="more">SEE MORE</span>
</section>

<section class="section" style="top:1578px">
  <div class="sec-title"><h2>PICKUP ITEMS</h2><p>ピックアップアイテム</p></div>
  <div class="grid">
    <article class="card"><div class="thumb t7" role="img" aria-label="商品写真:ニット"></div><span class="ribbon"></span><h3>アイテムタイトルアイテムタイトルアイテムタイトル</h3><div class="meta"><span class="cat">ITEMS</span><span class="date">¥0,000</span></div></article>
    <article class="card"><div class="thumb t8" role="img" aria-label="商品写真:スカーフ"></div><span class="ribbon"></span><h3>アイテムタイトルアイテムタイトルアイテムタイトル</h3><div class="meta"><span class="cat">ITEMS</span><span class="date">¥0,000</span></div></article>
    <article class="card"><div class="thumb t8" role="img" aria-label="商品写真:バッグ"></div><h3>アイテムタイトルアイテムタイトルアイテムタイトル</h3><div class="meta"><span class="cat">ITEMS</span><span class="date">¥0,000</span></div></article>
    <article class="card"><div class="thumb t5" role="img" aria-label="商品写真:ワンピース"></div><h3>アイテムタイトルアイテムタイトルアイテムタイトル</h3><div class="meta"><span class="cat">ITEMS</span><span class="date">¥0,000</span></div></article>
    <article class="card"><div class="thumb t9" role="img" aria-label="商品写真:アクセサリー"></div><h3>アイテムタイトルアイテムタイトルアイテムタイトル</h3><div class="meta"><span class="cat">ITEMS</span><span class="date">¥0,000</span></div></article>
    <article class="card"><div class="thumb t5" role="img" aria-label="商品写真:小物"></div><h3>アイテムタイトルアイテムタイトルアイテムタイトル</h3><div class="meta"><span class="cat">ITEMS</span><span class="date">¥0,000</span></div></article>
  </div>
  <span class="more">SEE MORE</span>
</section>

<aside class="sidebar">
  <div class="contact-btn">CONTACT</div>
  <div class="search"></div>
  <ul class="nav">
    <li>TOP</li><li>NEWS</li><li>ABOUT Rulavek</li><li>EVENT</li><li>BLOG</li><li>ITEMS</li>
  </ul>
  <div class="banner"><div class="ph" role="img" aria-label="バナー写真:ライター"></div></div>
  <div class="side-title"><h2>REVIEW</h2><p>お客様の声</p></div>
  <div class="review"><div class="img t6" role="img" aria-label="レビュー写真:バッグ"></div><span class="ribbon"></span><h3>お客様の声タイトル</h3><p>テキストテキストテキストテキストテキスト</p></div>
  <div class="review"><div class="img t7" role="img" aria-label="レビュー写真:トップス"></div><span class="ribbon"></span><h3>お客様の声タイトル</h3><p>テキストテキストテキストテキストテキスト</p></div>
  <div class="review"><div class="img t10" role="img" aria-label="レビュー写真:コート"></div><span class="ribbon"></span><h3>お客様の声タイトル</h3><p>テキストテキストテキストテキストテキスト</p></div>
  <div class="side-title" style="margin-top:30px"><h2>WRITER</h2><p>ライター紹介</p></div>
  <div class="writers">
    <div><div class="av" role="img" aria-label="ライター写真"></div>ライター名</div>
    <div><div class="av" role="img" aria-label="ライター写真"></div>ライター名</div>
  </div>
  <div class="side-title"><h2>KEYWORD</h2><p>キーワード</p></div>
  <div class="keywords"><span>コーデ</span><span>秋冬</span><span>ニット</span><span>バッグ</span><span>イベント</span><span>小物</span><span>着こなし</span><span>レビュー</span></div>
</aside>

<footer class="site-footer">
  <div class="wordmark">Rulavek</div>
  <div class="social"><span></span><span></span><span></span></div>
  <div class="foot-nav">
    <ul><li>TOP</li><li>NEWS</li><li>ABOUT Rulavek</li><li>EVENT</li><li>BLOG</li><li>ITEMS</li></ul>
    <ul><li>FAQ</li><li>WRITER</li><li>REVIEW</li><li>CONTACT</li></ul>
  </div>
  <div class="foot-contact"><div class="contact-btn">CONTACT</div></div>
  <span class="pagetop"></span>
  <p class="copy">Copyright © Rulavek All Rights Reserved.</p>
</footer>

</body>
</html>
```